Travel Company is looking for a STAND OUT Business Card

I need a unique Business Card that will truly stand out. Nothing too busy. Simple is good, right? Not looking for a standard design either. No cookie cutter layout. We are a Travel Company that works more with Companies than Travelers. I had an idea to focus and emphasis on the 2 logo a bit more. This is not necessary, however thought it would look interesting. I am just looking for something interesting and a bit different. Does't have to completely off the wall crazy, just not your run of the mill business card.

Target Market(s)

Hoteliers, Resort Management, Call Centers, Executives, Travelers, Families, Businesses

Industry/Entity Type

Hospitality

Contact Information for Business Card

President/CEO - Marcus T Bellamy (title not necessary if design doesn't allow for it)
contact - (407) 555-0186
email - mbellamy@wayfarenow.example
address - 4812 Quillmore Ave #164
Orlando, FL 32804
website - www.wayfarenow.example

Font styles to use
Serif
Other font styles liked:
• Avenir Next LT Pro BOLD

Requirements
Must have
• simple look and design. Unique design
Nice to have
• I attached the 2 logo separate from the main logo. This can be used separately from the Main Logo, together with the main logo or as main logo. I included the logo font. Use it or not, designers choice.
Should not have
• cookie cutter design. Little use of red other than the logo

```html
<!DOCTYPE html>
<html lang="en">
<head>
<meta charset="utf-8">
<title>Wayfare Now — Business Card</title>
<link rel="stylesheet" href="https://fonts.googleapis.com/css2?family=Nunito+Sans:wght@300;400;800;900&display=swap">
<style>
  :root {
    --stage: #3a3a3c;
    --card-dark: #4a4a4b;
    --card-light: #ffffff;
    --ink: #111111;
    --red: #e3222d;
    --grey: #8c8c8c;
  }
  * { margin: 0; padding: 0; box-sizing: border-box; }
  html, body { width: 1200px; height: 810px; overflow: hidden; background: var(--stage); }
  body { position: relative; font-family: "Nunito Sans", sans-serif; }

  .card {
    position: absolute;
    width: 560px;
    height: 320px;
    box-shadow: 0 10px 24px rgba(0,0,0,.35);
  }

  /* Back side */
  .card-back { left: 90px; top: 60px; background: var(--card-dark); display: flex; align-items: center; justify-content: center; }
  .card-back .brand { color: #ffffff; font-size: 40px; }

  /* Brand lockup */
  .brand { display: flex; align-items: center; gap: 12px; }
  .brand-dot { width: 18px; height: 18px; border-radius: 50%; background: var(--red); flex: none; }
  .brand-name { font-weight: 900; letter-spacing: -0.02em; line-height: 1; }

  /* Front side */
  .card-front { left: 550px; top: 430px; background: var(--card-light); }
  .card-front .brand { position: absolute; top: 42px; left: 0; right: 0; justify-content: center; color: var(--ink); font-size: 40px; }

  .person { position: absolute; left: 40px; top: 208px; width: 240px; text-align: right; }
  .person-name { color: var(--red); font-weight: 800; font-size: 24px; letter-spacing: 0.01em; text-transform: uppercase; line-height: 1.05; }
  .person-title { color: var(--grey); font-weight: 400; font-size: 14px; margin-top: 4px; }

  .divider { position: absolute; left: 300px; top: 150px; width: 1px; height: 140px;
    background: linear-gradient(to bottom, rgba(227,34,45,0), var(--red) 50%, rgba(227,34,45,0)); }

  .contact { position: absolute; left: 318px; top: 160px; list-style: none; color: var(--grey); font-weight: 300; font-size: 13.5px; line-height: 21px; }
  .contact li { display: flex; align-items: center; gap: 7px; white-space: nowrap; }
  .contact .no-icon { padding-left: 0; }
  .contact svg { width: 11px; height: 11px; flex: none; fill: none; stroke: var(--red); stroke-width: 1.6; }
  .contact .icon-fill { fill: var(--red); stroke: none; }
</style>
</head>
<body>

  <section class="card card-back">
    <div class="brand">
      <span class="brand-dot"></span>
      <span class="brand-name">wayfare now</span>
    </div>
  </section>

  <section class="card card-front">
    <div class="brand">
      <span class="brand-dot"></span>
      <span class="brand-name">wayfare now</span>
    </div>

    <div class="person">
      <p class="person-name">Marcus T Bellamy</p>
      <p class="person-title">President &amp; CEO</p>
    </div>

    <div class="divider"></div>

    <ul class="contact">
      <li>4812 Quillmore Ave #164</li>
      <li>Orlando, FL 32804</li>
      <li>
        <svg viewBox="0 0 12 12" aria-hidden="true"><path class="icon-fill" d="M2.5 1 L4.5 1 L5 3.5 L3.8 4.5 Q5 7 7.5 8.2 L8.5 7 L11 7.5 L11 9.5 Q10.5 11 9 11 Q1 10 1 3 Q1 1.5 2.5 1 Z"/></svg>
        (407) 555-0186
      </li>
      <li>
        <svg viewBox="0 0 12 12" aria-hidden="true"><rect class="icon-fill" x="0.5" y="2.5" width="11" height="7"/><path d="M0.8 2.8 L6 6.6 L11.2 2.8" stroke="#fff" stroke-width="1"/></svg>
        mbellamy@wayfarenow.example
      </li>
      <li>
        <svg viewBox="0 0 12 12" aria-hidden="true"><circle cx="6" cy="6" r="5"/><ellipse cx="6" cy="6" rx="2.2" ry="5"/><path d="M1 6 H11"/></svg>
        www.wayfarenow.example
      </li>
    </ul>
  </section>

</body>
</html>
```